TBW Construction
Stationary and Business Cards
Professional
Darek Venhollis
President
518 Marlow Ave
Brookvale, NJ 07999
tbwsonics@mailbox-example.com
tbwconstruction-example.com
NJ Lic# 58KT31720485
Commercial, Residential & Industrial

```html
<!DOCTYPE html>
<html lang="en">
<head>
<meta charset="utf-8">
<title>TBW Construction — Business Card</title>
<link href="https://fonts.googleapis.com/css2?family=Michroma&display=swap" rel="stylesheet">
<style>
  :root {
    --backdrop: #d9dadc;
    --card: #ffffff;
    --navy: #1f3a5f;
    --steel: #3d6fa8;
    --ink: #5b6672;
    --rule: #9aa5b1;
  }
  * { margin: 0; padding: 0; box-sizing: border-box; }
  html, body {
    width: 1200px; height: 895px; overflow: hidden;
    background: var(--backdrop);
    font-family: "Michroma", sans-serif;
  }
  .canvas { position: relative; width: 1200px; height: 895px; }
  .card {
    position: absolute; left: 250px; width: 700px; height: 400px;
    background: var(--card);
    box-shadow: 0 6px 18px rgba(0,0,0,.18);
  }
  .card--back { top: 35px; }
  .card--front { top: 460px; }

  .brand {
    display: flex; align-items: center; gap: 14px;
    color: var(--navy); font-size: 30px; letter-spacing: 2px;
    text-transform: uppercase; white-space: nowrap;
  }
  .brand__mark { width: 26px; height: 26px; background: var(--steel); }

  .card--back .brand { position: absolute; left: 50%; top: 150px; transform: translateX(-50%); }
  .website-line {
    position: absolute; left: 0; right: 0; top: 240px; text-align: center;
    font-size: 11px; letter-spacing: 5px; color: var(--ink); text-transform: uppercase;
  }

  .card--front .brand { position: absolute; left: 50%; top: 80px; transform: translateX(-50%); }
  .holder {
    position: absolute; left: 0; right: 0; top: 150px; text-align: center;
    font-size: 12px; letter-spacing: 3px; color: var(--ink); text-transform: uppercase;
  }
  .holder__sep { color: var(--rule); margin: 0 12px; }

  .contacts {
    position: absolute; left: 40px; right: 40px; bottom: 36px;
    display: grid; grid-template-columns: 1fr 1fr; gap: 12px 30px;
    font-size: 10.5px; color: var(--ink); letter-spacing: 1px;
  }
  .contact { display: flex; align-items: center; gap: 8px; white-space: nowrap; }
  .contact svg { width: 14px; height: 14px; flex: none; }
</style>
</head>
<body>
<div class="canvas">
  <section class="card card--back">
    <div class="brand"><span class="brand__mark"></span>TBW Construction</div>
    <p class="website-line">www.tbwconstruction-example.com</p>
  </section>

  <section class="card card--front">
    <div class="brand"><span class="brand__mark"></span>TBW Construction</div>
    <p class="holder">Darek Venhollis<span class="holder__sep">|</span>President</p>

    <div class="contacts">
      <div class="contact">
        <svg viewBox="0 0 14 14"><circle cx="7" cy="7" r="7" fill="var(--navy)"/><path d="M7 3.2a2.5 2.5 0 0 0-2.5 2.5C4.5 7.6 7 10.8 7 10.8s2.5-3.2 2.5-5.1A2.5 2.5 0 0 0 7 3.2z" fill="#fff"/></svg>
        518 Marlow Ave, Brookvale, NJ 07999
      </div>
      <div class="contact">
        <svg viewBox="0 0 14 14"><circle cx="7" cy="7" r="7" fill="var(--navy)"/><circle cx="7" cy="7" r="3.6" fill="none" stroke="#fff" stroke-width="1"/><path d="M3.4 7h7.2M7 3.4v7.2" stroke="#fff" stroke-width=".8"/></svg>
        www.tbwconstruction-example.com
      </div>
      <div class="contact">
        <svg viewBox="0 0 14 14"><circle cx="7" cy="7" r="7" fill="var(--navy)"/><path d="M4.6 3.6l1.4-.2.8 1.8-.9.7a5 5 0 0 0 2.2 2.2l.7-.9 1.8.8-.2 1.4c-3.4.4-6.2-2.4-5.8-5.8z" fill="#fff"/></svg>
        973-555-0142 &nbsp;|&nbsp; 973-555-0187
      </div>
      <div class="contact">
        <svg viewBox="0 0 14 14"><circle cx="7" cy="7" r="7" fill="var(--navy)"/><rect x="3.6" y="4.6" width="6.8" height="4.8" fill="#fff"/><path d="M3.6 4.6 7 7.4l3.4-2.8" fill="none" stroke="var(--navy)" stroke-width=".8"/></svg>
        tbwsonics@mailbox-example.com
      </div>
    </div>
  </section>
</div>
</body>
</html>
```